Truck Outfitters and Trailer Hitch Retailer Website

We are working with a hitch installer in California called Brisk Towline. They sell and install trailer hitches, bedliners for trucks, and pickup truck accessories.
Some sites to use for content/competitors:
https://www.valmareo.com/pick-up-outfitters
https://brennels-rigs.com
https://www.thetowlodge.com
https://towlodgeinccom.plumwebsites.com
Some sites to use for inspiration:
https://www.ironvaletows.com
https://quietlinkers.com
https://morvatow.com/
https://www.harborcoat.com
https://www.rugmark-trailworks.com
Thank you for taking the time to consider designing a website for us. We are web developers based in Stockton, CA, USA. Most of our projects go through the same process. Understanding this process may help you win a project with us. We custom-code all of our websites in-house. We don’t have any requirements as to what tools you use for your design, but we prefer Figma files. For any design that we label as four-stars, we send it to the client for review. The client picks the final design they want us to use. Once we complete this process, we will continue to show additional clients all the four-star sites and purchase them later. Your designs will have multiple chances to sell. For better chances of success, we ask that you follow these guidelines.
IMAGES:
If you use any images or icons in the design, we ask that you have a link to the asset so we can purchase the image/icon. Most of the designs we submit do not have the customer’s images on them unless they have some great images. Be creative; show us the feeling you are trying to portray with your image choices. Use any royalty-free site you choose. We subscribe to Adobe and mainly use their images, but we can purchase images outside of Adobe.
PLEASE NOTE: we will not submit designs to clients with watermarks on the images.
FONTS:
We ask that you identify the fonts used in the design. This can be done in a message if you want. We typically use Google Fonts and Adobe Fonts.
CONTENT:
We're always open to different content and ideas. We often submit designs with stock images so the client can see our vision. We typically take pictures after the website launch to use their images with our vision. Lorem Ipsum is fine for paragraphs, but we ask that you write the headers in correct English. We want to be able to show the vision and identify the sections of the website.
INSPIRATION:
We typically add a couple of links in the brief of websites we like to help you get started in your design.
REVISIONS:
We do not often ask for revisions of the designs unless we see something in the design that may not appeal to the client. If there are slight changes that we want to make, we do that in the development process.
FEEDBACK:
We rarely give feedback on designs during the design process. We are working on many website projects and do not have the time to provide feedback. We usually respond if your request is well thought out and asks specific questions, but a note asking “feedback, please” usually goes unanswered

```html
<!DOCTYPE html>
<html lang="en">
<head>
<meta charset="utf-8">
<title>Brisk Towline — Trailer Hitches &amp; Truck Accessories</title>
<link rel="stylesheet" href="https://fonts.googleapis.com/css2?family=Michroma&family=Poppins:wght@300;400;500;600;700&display=swap">
<style>
:root{
  --red:#e3120b;
  --red-dark:#b80d08;
  --black:#0b0b0b;
  --ink:#151515;
  --grey:#555;
  --light:#f4f4f4;
  --line:#d9d9d9;
  --white:#fff;
}
*{box-sizing:border-box;margin:0;padding:0}
html,body{width:1200px;height:5276px;overflow:hidden}
body{position:relative;font-family:'Poppins',sans-serif;color:var(--ink);background:var(--white)}
.section{position:absolute;left:0;width:1200px;overflow:hidden}
.display{font-family:'Michroma',sans-serif;text-transform:uppercase;font-weight:400}
.accent{color:var(--red)}
.btn{display:inline-block;background:var(--red);color:var(--white);font-size:13px;font-weight:600;text-transform:uppercase;padding:12px 24px;letter-spacing:.5px;clip-path:polygon(0 0,100% 0,92% 100%,0 100%)}
.body-copy{font-size:13px;line-height:1.75;color:var(--grey)}
.photo{position:absolute}

/* Hero */
.hero{top:0;height:992px;background:#222}
.hero-photo{inset:0;background:linear-gradient(120deg,#5a2a18 0%,#7a4a36 18%,#3d3a3a 45%,#2a3347 70%,#1c1c20 100%)}
.hero-shade{position:absolute;inset:0;background:rgba(0,0,0,.45)}
.site-header{position:absolute;top:0;left:0;width:1200px;height:120px;display:flex;align-items:center;padding:0 64px}
.brand{font-family:'Poppins',sans-serif;font-weight:700;text-transform:uppercase;display:flex;align-items:center;gap:10px;color:var(--white)}
.brand-dot{width:18px;height:18px;border-radius:50%;background:var(--red)}
.site-header .brand{font-size:26px}
.nav{margin-left:auto;display:flex;gap:34px;align-items:center;font-size:14px;color:var(--white)}
.nav .current{color:var(--red)}
.nav .btn{clip-path:none;padding:9px 18px;font-size:13px;text-transform:none}
.hero-copy{position:absolute;top:400px;left:0;width:1200px;text-align:center;color:var(--white)}
.hero-copy .welcome{font-size:38px;font-weight:600}
.hero-copy .brand-title{font-family:'Poppins',sans-serif;font-weight:700;font-size:76px;text-transform:uppercase;letter-spacing:2px;line-height:1.15}
.hero-copy .tagline{font-size:26px;font-weight:600;margin-top:10px}
.hero-copy .btn{margin-top:28px}

/* About */
.about{top:992px;height:676px;background:var(--white)}
.about-frame{position:absolute;left:0;top:128px;width:540px;height:436px;background:var(--red);clip-path:polygon(0 0,82% 0,100% 100%,0 100%)}
.about-photo{left:0;top:136px;width:520px;height:420px;background:linear-gradient(135deg,#4a5260,#8a8f98 40%,#2f3a4e 75%,#1d2330);clip-path:polygon(0 0,80% 0,98% 100%,0 100%)}
.about-copy{position:absolute;left:660px;top:180px;width:480px}
.heading-lg{font-size:40px;line-height:1.1}
.sub-label{font-size:13px;font-weight:600;margin:6px 0 20px}
.about-copy .body-copy{margin-bottom:14px}
.about-copy .btn{margin-top:16px}

/* Services */
.services{top:1668px;height:876px;background:var(--black);color:var(--white)}
.services-head{position:absolute;left:100px;top:128px;width:1000px}
.services-head .sub-label{color:var(--white);margin-bottom:22px}
.services-head .body-copy{color:#bbb;font-size:12px}
.slider-arrows{position:absolute;right:80px;top:140px;display:flex;gap:12px}
.arrow-btn{width:40px;height:40px;border-radius:50%;display:flex;align-items:center;justify-content:center}
.arrow-btn.muted{background:#333}
.arrow-btn.active{background:#888}
.service-card{position:absolute;top:372px;width:324px}
.service-photo{position:relative;height:312px;background:var(--red)}
.service-photo .fill{position:absolute;inset:0 0 0 0;clip-path:polygon(0 0,92% 0,100% 100%,0 100%)}
.service-card h3{font-size:14px;font-weight:500;text-transform:uppercase;text-align:center;margin-top:22px}
.service-card.featured h3{color:var(--red)}
.plus{width:24px;height:24px;background:var(--red);margin:12px auto 0;display:flex;align-items:center;justify-content:center}

/* Banner */
.banner{top:2544px;height:568px;background:var(--black)}
.banner-photo{left:0;top:0;width:720px;height:568px;background:linear-gradient(140deg,#6d6d6b,#9b958d 35%,#3b3a38 70%,#1f1f1e)}
.banner-panel{position:absolute;right:0;top:0;width:640px;height:568px;background:var(--black);clip-path:polygon(18% 0,100% 0,100% 100%,0 100%)}
.banner-copy{position:absolute;right:60px;top:110px;width:560px;text-align:right;color:var(--white)}
.banner-copy h2{font-size:25px;line-height:1.62}
.banner-copy .btn{margin-top:30px}

/* Testimonials */
.testimonials{top:3112px;height:1008px;background:var(--white)}
.t-head{position:absolute;top:200px;left:0;width:1200px;text-align:center}
.t-head .sub-label{display:flex;align-items:center;justify-content:center;gap:12px}
.t-head .sub-label::before,.t-head .sub-label::after{content:"";width:60px;height:1px;background:var(--ink)}
.t-band{left:68px;top:360px;width:1064px;height:440px;background:linear-gradient(180deg,#7e8ea3 0%,#5f6e82 45%,#3a3b3a 80%,#2a2a28)}
.t-band-shade{position:absolute;left:68px;top:360px;width:1064px;height:440px;background:rgba(0,0,0,.55)}
.quote{position:absolute;top:416px;width:420px;color:var(--white)}
.quote-mark{font-size:54px;font-weight:700;line-height:.6;margin-bottom:10px}
.quote p{font-size:13px;line-height:1.7;color:#e6e6e6}
.author{display:flex;align-items:center;gap:14px;margin-top:24px}
.avatar{width:72px;height:72px;border-radius:50%;background:#c9c9c9;border:3px solid var(--white)}
.author strong{display:block;font-size:13px;font-weight:600}
.stars{color:#f5b301;font-size:14px;letter-spacing:1px}
.side-arrow{position:absolute;top:560px;width:36px;height:36px;border-radius:50%;display:flex;align-items:center;justify-content:center}
.side-arrow.left{left:8px;background:#eee}
.side-arrow.right{right:8px;background:var(--red)}
.dots{position:absolute;top:856px;left:0;width:1200px;display:flex;justify-content:center;gap:12px}
.dots span{width:10px;height:10px;border-radius:50%;background:#ccc}
.dots span.on{background:var(--red)}

/* Contact */
.contact{top:4120px;height:580px;background:var(--white)}
.contact-photo{left:0;top:40px;width:520px;height:480px;background:linear-gradient(150deg,#8d8f90,#c6c4bf 35%,#5b5e60 65%,#2e3032);clip-path:polygon(0 0,100% 0,82% 100%,0 100%)}
.contact-copy{position:absolute;left:620px;top:40px;width:520px}
.contact-copy .body-copy{margin-top:10px;font-size:12px}
.form{position:absolute;left:620px;top:200px;width:508px;display:grid;grid-template-columns:1fr 1fr;gap:22px 28px}
.field{height:50px;border:1px solid var(--line);padding:0 16px;display:flex;align-items:center;font-size:13px;color:#999}
.field.wide{grid-column:1/3;height:100px;align-items:flex-start;padding-top:14px}
.form .btn{grid-column:1/2;width:150px;text-align:center;margin-top:8px}

/* Footer */
.footer{top:4700px;height:520px;background:var(--black);color:var(--white)}
.footer-brand{position:absolute;left:96px;top:130px;width:260px;text-align:center}
.footer-brand .brand{font-size:30px;justify-content:center}
.social{display:flex;gap:18px;justify-content:center;margin-top:34px}
.social span{width:18px;height:18px;border-radius:50%;background:var(--red)}
.footer-col{position:absolute;top:118px}
.footer-col h4{font-size:14px;font-weight:600;color:var(--red);text-transform:uppercase;margin-bottom:22px}
.links li{list-style:none;font-size:14px;margin-bottom:10px;display:flex;align-items:center;gap:10px}
.contact-item{display:flex;gap:14px;margin-bottom:20px;font-size:13px;line-height:1.5}
.icon-box{width:28px;height:28px;background:var(--red);flex:none;display:flex;align-items:center;justify-content:center}
.newsletter p{font-size:13px;line-height:1.6;margin-bottom:22px}
.subscribe{display:flex;width:220px;height:40px;border:1px solid #555}
.subscribe span{flex:1;font-size:12px;color:#999;display:flex;align-items:center;padding-left:12px}
.subscribe .go{flex:none;width:40px;background:var(--red);justify-content:center;padding:0}
.copyright{top:5220px;height:56px;background:var(--red);color:var(--white);font-size:12px;display:flex;align-items:center;justify-content:center}
</style>
</head>
<body>

<section class="section hero">
  <div class="photo hero-photo" role="img" aria-label="Mechanic kneeling beside an orange pickup truck wheel, installing a hitch"></div>
  <div class="hero-shade"></div>
  <header class="site-header">
    <div class="brand"><span class="brand-dot"></span>Brisk Towline</div>
    <nav class="nav">
      <span class="current">Home</span><span>About</span><span>Services</span><span>Products</span><span>Photo Gallery</span><span>Testimonials</span><span class="btn">Contact</span>
    </nav>
  </header>
  <div class="hero-copy">
    <p class="welcome">Welcome to</p>
    <h1 class="brand-title">Brisk Towline</h1>
    <p class="tagline">We are working with a hitch installer in California</p>
    <span class="btn">Contact us &#8599;</span>
  </div>
</section>

<section class="section about">
  <div class="about-frame"></div>
  <div class="photo about-photo" role="img" aria-label="Two mechanics working under a lifted car in a workshop"></div>
  <div class="about-copy">
    <h2 class="display heading-lg">About <span class="accent">Us</span></h2>
    <p class="sub-label">Who We Are</p>
    <p class="body-copy">Lorem ipsum dolor sit amet, consectetur adipiscing elit, sed do eiusmod tempor incididunt ut labore et dolore magna aliqua. Quis ipsum suspendisse ultrices gravida. Risus commodo viverra maecenas accumsan lacus vel facilisis.</p>
    <p class="body-copy">Lorem ipsum dolor sit amet, consectetur adipiscing elit, sed do eiusmod tempor incididunt ut labore et dolore magna aliqua. Quis ipsum suspendisse ultrices gravida. Risus commodo viverra maecenas accumsan lacus vel facilisis.</p>
    <span class="btn">Know more &#8599;</span>
  </div>
</section>

<section class="section services">
  <div class="services-head">
    <h2 class="display heading-lg">Our <span class="accent">Services</span></h2>
    <p class="sub-label">What We Do</p>
    <p class="body-copy">Lorem ipsum dolor sit amet, consectetur adipiscing elit, sed do eiusmod tempor incididunt ut labore et dolore magna aliqua. Quis ipsum suspendisse ultrices gravida. Risus commodo viverra maecenas accumsan lacus vel facilisis.</p>
  </div>
  <div class="slider-arrows">
    <span class="arrow-btn muted"><svg width="14" height="14" viewBox="0 0 14 14"><path d="M9 2 4 7l5 5" fill="none" stroke="#888" stroke-width="2"/></svg></span>
    <span class="arrow-btn active"><svg width="14" height="14" viewBox="0 0 14 14"><path d="M5 2l5 5-5 5" fill="none" stroke="#fff" stroke-width="2"/></svg></span>
  </div>
  <article class="service-card" style="left:68px">
    <div class="service-photo"><div class="fill" role="img" aria-label="Mechanic fitting a hitch to a truck wheel area" style="background:linear-gradient(140deg,#c8ccd0,#7e8690 45%,#2b2f35)"></div></div>
    <h3>Sell and install trailer hitches</h3>
  </article>
  <article class="service-card featured" style="left:440px">
    <div class="service-photo"><div class="fill" role="img" aria-label="Black pickup truck with a protected bed in a garage" style="background:linear-gradient(140deg,#5d5d5d,#2a2a2a 55%,#111)"></div></div>
    <h3>Bedliners for trucks</h3>
    <div class="plus"><svg width="10" height="10" viewBox="0 0 10 10"><path d="M5 0v10M0 5h10" stroke="#fff" stroke-width="2"/></svg></div>
  </article>
  <article class="service-card" style="left:812px">
    <div class="service-photo"><div class="fill" role="img" aria-label="Chrome wrenches and gear parts laid out" style="background:linear-gradient(140deg,#e2e2e2,#9c9c9c 45%,#4a4a4a)"></div></div>
    <h3>Pickup truck accessories</h3>
  </article>
</section>

<section class="section banner">
  <div class="photo banner-photo" role="img" aria-label="Close-up of a trailer coupler and safety chain"></div>
  <div class="banner-panel"></div>
  <div class="banner-copy">
    <h2 class="display">We do all types of trailer towing products such as hitch installation, brakes, bearings, wiring and everything in between</h2>
    <span class="btn">Contact us &#8599;</span>
  </div>
</section>

<section class="section testimonials">
  <div class="t-head">
    <h2 class="display heading-lg">Our <span class="accent">Testimonials</span></h2>
    <p class="sub-label">What Our Clients Says</p>
  </div>
  <div class="photo t-band" role="img" aria-label="Empty flatbed trailer parked under an open sky"></div>
  <div class="t-band-shade"></div>
  <div class="quote" style="left:140px">
    <div class="quote-mark">&ldquo;</div>
    <p>Lorem ipsum dolor sit amet, consectetur adipiscing elit, sed do eiusmod tempor incididunt ut labore et dolore magna aliqua. Quis ipsum suspendisse ultrices gravida risus commodo viverra.</p>
    <div class="author"><span class="avatar" role="img" aria-label="Client portrait"></span><div><strong>Marcus Delano</strong><span class="stars">&#9733;&#9733;&#9733;&#9733;&#9733;</span></div></div>
  </div>
  <div class="quote" style="left:660px">
    <div class="quote-mark">&ldquo;</div>
    <p>Lorem ipsum dolor sit amet, consectetur adipiscing elit, sed do eiusmod tempor incididunt ut labore et dolore magna aliqua. Quis ipsum suspendisse ultrices gravida risus commodo viverra.</p>
    <div class="author"><span class="avatar" role="img" aria-label="Client portrait"></span><div><strong>Marcus Delano</strong><span class="stars">&#9733;&#9733;&#9733;&#9733;&#9733;</span></div></div>
  </div>
  <span class="side-arrow left"><svg width="12" height="12" viewBox="0 0 12 12"><path d="M8 2 4 6l4 4" fill="none" stroke="#333" stroke-width="2"/></svg></span>
  <span class="side-arrow right"><svg width="12" height="12" viewBox="0 0 12 12"><path d="M4 2l4 4-4 4" fill="none" stroke="#fff" stroke-width="2"/></svg></span>
  <div class="dots"><span class="on"></span><span></span><span></span></div>
</section>

<section class="section contact">
  <div class="photo contact-photo" role="img" aria-label="Close-up of a steel trailer hitch latch"></div>
  <div class="contact-copy">
    <h2 class="display heading-lg">Contact <span class="accent">Us</span></h2>
    <p class="body-copy">Lorem ipsum dolor sit amet, consectetur adipiscing elit, sed do eiusmod tempor incididunt ut labore et dolore magna aliqua. Quis ipsum suspendisse ultrices gravida.</p>
  </div>
  <div class="form">
    <div class="field">First Name</div><div class="field">Last Name</div>
    <div class="field">Phone</div><div class="field">Email</div>
    <div class="field wide">Message</div>
    <span class="btn">Submit</span>
  </div>
</section>

<footer class="section footer">
  <div class="footer-brand">
    <div class="brand"><span class="brand-dot"></span>Brisk Towline</div>
    <div class="social"><span></span><span></span><span></span></div>
  </div>
  <div class="footer-col" style="left:392px">
    <h4>Quick Links</h4>
    <ul class="links">
      <li><svg width="12" height="12" viewBox="0 0 12 12"><path d="M1 6l3 3 7-7" fill="none" stroke="#e3120b" stroke-width="2"/></svg>About Us</li>
      <li><svg width="12" height="12" viewBox="0 0 12 12"><path d="M1 6l3 3 7-7" fill="none" stroke="#e3120b" stroke-width="2"/></svg>Services</li>
      <li><svg width="12" height="12" viewBox="0 0 12 12"><path d="M1 6l3 3 7-7" fill="none" stroke="#e3120b" stroke-width="2"/></svg>Products</li>
      <li><svg width="12" height="12" viewBox="0 0 12 12"><path d="M1 6l3 3 7-7" fill="none" stroke="#e3120b" stroke-width="2"/></svg>Testimonials</li>
      <li><svg width="12" height="12" viewBox="0 0 12 12"><path d="M1 6l3 3 7-7" fill="none" stroke="#e3120b" stroke-width="2"/></svg>Contact Us</li>
    </ul>
  </div>
  <div class="footer-col" style="left:620px;width:260px">
    <h4>Contact Us</h4>
    <div class="contact-item"><span class="icon-box"><svg width="14" height="14" viewBox="0 0 14 14"><path d="M3 1l2 3-1.5 1.5a8 8 0 0 0 5 5L10 9l3 2-1.5 2.5C6 13 1 8 .5 2.5z" fill="#fff"/></svg></span><div>CALL US<br>(800) 555-0142</div></div>
    <div class="contact-item"><span class="icon-box"><svg width="14" height="12" viewBox="0 0 14 12"><rect x="1" y="1" width="12" height="10" fill="none" stroke="#fff" stroke-width="1.5"/><path d="M1 1l6 5 6-5" fill="none" stroke="#fff" stroke-width="1.5"/></svg></span><div>EMAIL US<br>info@brisktowline.com</div></div>
    <div class="contact-item"><span class="icon-box"><svg width="12" height="14" viewBox="0 0 12 14"><path d="M6 0a5 5 0 0 0-5 5c0 4 5 9 5 9s5-5 5-9a5 5 0 0 0-5-5z" fill="#fff"/><circle cx="6" cy="5" r="2" fill="#e3120b"/></svg></span><div>Address line sample text<br>Address line two</div></div>
  </div>
  <div class="footer-col newsletter" style="left:920px;width:220px">
    <h4>Our Newsletter</h4>
    <p>Subscribe our newsletter to get the latest news.</p>
    <div class="subscribe"><span>Enter Email Address</span><span class="go"><svg width="12" height="12" viewBox="0 0 12 12"><path d="M4 2l4 4-4 4" fill="none" stroke="#fff" stroke-width="2"/></svg></span></div>
  </div>
</footer>
<div class="section copyright">Copyright &copy; 2024 All Rights Reserved By Brisk Towline</div>

</body>
</html>
```